Pebble

My company name is pebble. The logo is attached. I am the business owner.
Name Gideon Thorpe
Phone number- 5553018826
email- Gideon_thorpe@quillnet.net
Website is not live yet but it will be workwithpebble.com
the current beta link is- https://site.brvhosting.com/pebble-v3/
on the back write “ find creative pros”
Use that beta link as reference for typography and colors on card.

```html
<!DOCTYPE html>
<html lang="en">
<head>
<meta charset="utf-8">
<title>Pebble – Business Card</title>
<link href="https://fonts.googleapis.com/css2?family=Arimo:wght@400;700&display=swap" rel="stylesheet">
<style>
  :root {
    --backdrop: #2b2b2b;
    --card-front: #d4d4d4;
    --card-back: #ffffff;
    --ink-white: #ffffff;
    --ink-grey: #d2d2d2;
    --ink-soft: #c9c9c9;
  }
  * { margin: 0; padding: 0; box-sizing: border-box; }
  html, body {
    width: 1200px; height: 900px; overflow: hidden;
    background: var(--backdrop);
    font-family: "Arimo", Arial, sans-serif;
  }
  .stage {
    width: 1200px; height: 900px;
    display: flex; flex-direction: column;
    align-items: center; justify-content: center; gap: 40px;
  }
  .card {
    position: relative;
    width: 700px; height: 400px;
    border-radius: 34px;
    overflow: hidden;
  }
  .card--front { background: var(--card-front); }
  .card--back { background: var(--card-back); }

  .brand-name {
    font-weight: 700;
    letter-spacing: 2px;
    line-height: 1;
  }
  .card--front .brand-name {
    position: absolute; left: 0; right: 0; top: 132px;
    text-align: center;
    font-size: 104px; color: var(--ink-white);
  }
  .tagline {
    position: absolute; left: 0; right: 0; top: 284px;
    text-align: center;
    font-size: 20px; letter-spacing: 1px;
    color: var(--ink-white);
  }

  .card--back .brand-name {
    position: absolute; left: 70px; top: 58px;
    font-size: 92px; color: var(--ink-grey);
  }
  .holder-name {
    position: absolute; left: 70px; top: 300px;
    font-size: 27px; font-weight: 700; letter-spacing: 1px;
    color: var(--ink-grey);
  }
  .divider {
    position: absolute; left: 360px; top: 185px;
    width: 2px; height: 145px;
    background: var(--ink-soft);
  }
  .contact-list {
    position: absolute; left: 385px; top: 182px;
    list-style: none;
  }
  .contact-item {
    display: flex; align-items: center; gap: 12px;
    height: 36px;
    font-size: 20px; color: var(--ink-grey);
  }
  .contact-icon { width: 18px; height: 18px; flex: none; }
</style>
</head>
<body>
  <main class="stage">
    <section class="card card--front">
      <div class="brand-name">PEBBLE</div>
      <p class="tagline">FIND CREATIVE PROS</p>
    </section>

    <section class="card card--back">
      <div class="brand-name">PEBBLE</div>
      <p class="holder-name">GIDEON THORPE</p>
      <div class="divider"></div>
      <ul class="contact-list">
        <li class="contact-item">
          <svg class="contact-icon" viewBox="0 0 24 24"><path fill="#c9c9c9" d="M6.6 10.8a15.1 15.1 0 0 0 6.6 6.6l2.2-2.2a1 1 0 0 1 1-.25 11.4 11.4 0 0 0 3.6.57 1 1 0 0 1 1 1V20a1 1 0 0 1-1 1A17 17 0 0 1 3 4a1 1 0 0 1 1-1h3.5a1 1 0 0 1 1 1c0 1.25.2 2.45.57 3.57a1 1 0 0 1-.25 1z"/></svg>
          <span>5553018826</span>
        </li>
        <li class="contact-item">
          <svg class="contact-icon" viewBox="0 0 24 24"><path fill="#c9c9c9" d="M2 5h20v14H2z"/><path fill="none" stroke="#fff" stroke-width="1.8" d="M2.5 5.5 12 13l9.5-7.5"/></svg>
          <span>Gideon_thorpe@quillnet.net</span>
        </li>
        <li class="contact-item">
          <svg class="contact-icon" viewBox="0 0 24 24"><circle cx="12" cy="12" r="10" fill="#c9c9c9"/><path fill="none" stroke="#fff" stroke-width="1.6" d="M2 12h20M12 2c3 3 3 17 0 20M12 2c-3 3-3 17 0 20"/></svg>
          <span>workwithpebble.com</span>
        </li>
        <li class="contact-item">
          <svg class="contact-icon" viewBox="0 0 24 24"><circle cx="12" cy="12" r="10" fill="#c9c9c9"/><path fill="none" stroke="#fff" stroke-width="1.6" d="M2 12h20M12 2c3 3 3 17 0 20M12 2c-3 3-3 17 0 20"/></svg>
          <span>site.brvhosting.com/pebble-v3/</span>
        </li>
      </ul>
    </section>
  </main>
</body>
</html>
```